Corp. Logo & Business Card for KVT Printing Services Ltd.

We have been in business 40 years need a stunding Corp.
Logo that shows great 3D graphics & is bright in colors so
our customers will want us to design their Corp. Logos & do their Printing. just for your information, I like Colors Maroon,
Yellow, Red etc. You do not have to stay with these colors if you have a better color design. The KVT Logo I would like a Very distinctive Font & can be Mulit Color.
I have attached what we are using now, I like the Red Gold with the bright sun light
behind the copy to attach attention.

KVT
Dorwen Services Ltd.
P.O. Box 4630, Brea, CA 92817
714.389.4125 ext. 316
714.389.4190 Fax
wade @ mytradeworkshop-sample.com
www.kvtcardworks-sample.com

KVT
Dorwen Services Ltd.
714.389.4125 ext. 316
714.389.4190 Fax

Dear Designers; You all did a great job.

Thanks

Wade Benfield

```html
<!DOCTYPE html>
<html lang="en">
<head>
<meta charset="utf-8">
<title>KVT Printing Services Ltd. — Business Card</title>
<link rel="stylesheet" href="https://fonts.googleapis.com/css2?family=Bitter:wght@700&display=swap">
<style>
  :root {
    --card-bg: #eeedea;
    --accent: #d9772b;
    --ink: #141414;
    --icon-fg: #ffffff;
  }
  html, body {
    margin: 0;
    padding: 0;
    overflow: hidden;
    background: var(--card-bg);
  }
  .card {
    position: relative;
    width: 1200px;
    height: 686px;
    overflow: hidden;
    background: var(--card-bg);
    font-family: "Bitter", Georgia, serif;
    font-weight: 700;
    color: var(--ink);
  }
  .brand {
    position: absolute;
    left: 165px;
    top: 78px;
    display: flex;
    align-items: center;
    gap: 34px;
  }
  .brand-disc {
    width: 172px;
    height: 172px;
    border-radius: 50%;
    background: var(--accent);
    flex: none;
  }
  .brand-name {
    margin: 0;
    font-size: 66px;
    line-height: 1.05;
    color: var(--accent);
    font-weight: 700;
    letter-spacing: 1px;
  }
  .contact {
    position: absolute;
    display: flex;
    align-items: center;
    margin: 0;
    white-space: nowrap;
  }
  .contact .icon {
    flex: none;
    width: 44px;
    height: 44px;
    border-radius: 50%;
    background: var(--accent);
    display: flex;
    align-items: center;
    justify-content: center;
  }
  .contact .icon svg { width: 24px; height: 24px; }
  .contact--large { font-size: 31px; }
  .contact--small { font-size: 21px; }
  .contact--large .label { margin-left: 14px; }
  .contact--small .label { margin-left: 20px; }

  .phone   { left: 170px; top: 332px; }
  .fax     { left: 685px; top: 332px; }
  .web     { left: 170px; top: 471px; }
  .email   { left: 685px; top: 471px; }
  .address { left: 353px; top: 600px; }
  .fax .label { margin-left: 32px; }
</style>
</head>
<body>
<main class="card">
  <header class="brand">
    <div class="brand-disc"></div>
    <h1 class="brand-name">KVT Printing<br>Services</h1>
  </header>

  <p class="contact contact--large phone">
    <span class="icon">
      <svg viewBox="0 0 24 24" fill="var(--icon-fg)"><path d="M6.6 10.8a15.2 15.2 0 0 0 6.6 6.6l2.2-2.2a1 1 0 0 1 1-.25 11.4 11.4 0 0 0 3.6.57 1 1 0 0 1 1 1V20a1 1 0 0 1-1 1A17 17 0 0 1 3 4a1 1 0 0 1 1-1h3.5a1 1 0 0 1 1 1c0 1.25.2 2.45.57 3.57a1 1 0 0 1-.25 1z"/></svg>
    </span>
    <span class="label">714.389.4125 ext. 316</span>
  </p>

  <p class="contact contact--large fax">
    <span class="icon">
      <svg viewBox="0 0 24 24" fill="var(--icon-fg)"><path d="M6.6 10.8a15.2 15.2 0 0 0 6.6 6.6l2.2-2.2a1 1 0 0 1 1-.25 11.4 11.4 0 0 0 3.6.57 1 1 0 0 1 1 1V20a1 1 0 0 1-1 1A17 17 0 0 1 3 4a1 1 0 0 1 1-1h3.5a1 1 0 0 1 1 1c0 1.25.2 2.45.57 3.57a1 1 0 0 1-.25 1z"/></svg>
    </span>
    <span class="label">714.389.4190 Fax</span>
  </p>

  <p class="contact contact--small web">
    <span class="icon">
      <svg viewBox="0 0 24 24" fill="none" stroke="var(--icon-fg)" stroke-width="2.6" stroke-linecap="round"><path d="M10 14a4 4 0 0 0 5.7 0l3-3a4 4 0 0 0-5.7-5.7l-1.2 1.2"/><path d="M14 10a4 4 0 0 0-5.7 0l-3 3a4 4 0 0 0 5.7 5.7l1.2-1.2"/></svg>
    </span>
    <span class="label">www.kvtcardworks-sample.com</span>
  </p>

  <p class="contact contact--small email">
    <span class="icon">
      <svg viewBox="0 0 24 24" fill="var(--icon-fg)"><path d="M3 6.5A1.5 1.5 0 0 1 4.5 5h15A1.5 1.5 0 0 1 21 6.5v.3l-9 5.6-9-5.6z"/><path d="M3 9.2l9 5.6 9-5.6v8.3a1.5 1.5 0 0 1-1.5 1.5h-15A1.5 1.5 0 0 1 3 17.5z"/></svg>
    </span>
    <span class="label">wade @ mytradeworkshop-sample.com</span>
  </p>

  <p class="contact contact--large address">
    <span class="icon">
      <svg viewBox="0 0 24 24" fill="var(--icon-fg)"><path d="M12 3l9.5 8.5h-3V20h-4.5v-5.5h-4V20H5.5v-8.5h-3z"/></svg>
    </span>
    <span class="label">P.O. Box 4630, Brea, CA 92817</span>
  </p>
</main>
</body>
</html>
```